Capability Statement Document/Flyer

Take the existing words from the capability statement document (attached) and design a unique folder/flyer document for professional use. Maybe something like a trifold or bifold style. Use approved colours and logo as per the attached files.
Our company designs and builds small onshore gas processing plants.

```html
<!DOCTYPE html>
<html lang="en">
<head>
<meta charset="utf-8">
<title>Corvanta Capability Statement</title>
<link rel="stylesheet" href="https://fonts.googleapis.com/css2?family=Inter:ital,wght@0,300;0,400;0,500;0,600;0,700;1,400&family=IBM+Plex+Mono:wght@400;500&display=swap">
<style>
:root{
  --bg:#d9d9d8;
  --paper:#f7f6f3;
  --forest:#07302b;
  --teal:#087a68;
  --teal-soft:#e6efec;
  --ink:#1a1a1a;
  --grey:#6f6f6f;
  --line:#d6d6d2;
  --gold:#b68b2e;
}
*{margin:0;padding:0;box-sizing:border-box}
html,body{width:889px;height:1200px;overflow:hidden;background:var(--bg);font-family:"Inter",sans-serif;color:var(--ink)}
.page{position:absolute;width:400px;height:566px;background:var(--paper);overflow:hidden}
.p1{left:38px;top:28px;background:var(--forest)}
.p2{left:452px;top:28px}
.p3{left:38px;top:606px}
.p4{left:452px;top:606px}
.abs{position:absolute}
.mono{font-family:"IBM Plex Mono",monospace}
.runner{position:absolute;top:12px;left:28px;right:28px;display:flex;justify-content:space-between;font-size:4.5px;color:#9a9a96;letter-spacing:.4px;border-bottom:.5px solid var(--line);padding-bottom:4px}
.folio{position:absolute;bottom:16px;left:28px;right:28px;display:flex;justify-content:space-between;font-size:4.5px;color:#a5a5a1}
.eyebrow{font-family:"IBM Plex Mono",monospace;font-size:5.5px;line-height:7px;letter-spacing:2px;color:var(--teal);font-weight:500}
h2{font-size:17px;line-height:19px;font-weight:600;letter-spacing:-.2px;color:var(--ink)}
.lead{font-size:6.2px;line-height:9.6px;color:var(--grey);font-weight:300}
/* cover */
.cover-photo{position:absolute;left:0;top:0;width:400px;height:279px;background:linear-gradient(180deg,#c9c9c4 0%,#b4b5b0 55%,#6d706c 80%,#3b3e3c 100%)}
.brand{font-size:17px;font-weight:600;letter-spacing:1px;color:var(--teal)}
.cover-brand{position:absolute;top:325px;width:100%;text-align:center}
.cover-kicker{position:absolute;top:386px;width:100%;text-align:center;font-family:"IBM Plex Mono",monospace;font-size:5.4px;letter-spacing:2px;color:#2f9a86}
.cover-title{position:absolute;top:398px;width:100%;text-align:center;font-size:29px;line-height:36px;font-weight:400;color:#fff;letter-spacing:-.3px}
.cover-sub{position:absolute;top:441px;width:100%;text-align:center;font-size:7.5px;font-style:italic;color:#e2e7e5}
.stats{position:absolute;top:472px;left:0;width:100%;display:flex;justify-content:center}
.stat{width:57px;text-align:center;border-right:.6px solid #2a6a5f}
.stat:last-child{border-right:none}
.stat b{display:block;font-size:10.5px;font-weight:500;color:#fff}
.stat span{display:block;font-size:4.2px;letter-spacing:.6px;color:#7fa59d;margin-top:4px}
.cover-rule{position:absolute;top:507px;left:140px;width:120px;border-top:.6px solid #2a6a5f}
.cover-url{position:absolute;top:514px;width:100%;text-align:center;font-size:6px;font-style:italic;color:#e2e7e5}
/* people */
.card{position:absolute;width:165px;height:132px;background:#fff;border:.6px solid var(--line);border-left:3px solid var(--teal);border-radius:0 0 4px 4px}
.card-head{background:var(--teal);height:33px;padding:7px 0 0 14px;color:#fff;border-radius:3px 3px 0 0;margin-left:-3px}
.card-head h3{font-size:9.5px;font-weight:600}
.card-head p{font-size:5.5px;color:#bfe0d8;margin-top:1px}
.card-body{padding:5px 10px 0 11px}
.card-exp{font-family:"IBM Plex Mono",monospace;font-size:4.2px;line-height:6px;color:#555}
.card-exp i{font-style:normal;color:#999}
.card-text{font-size:5px;line-height:7.7px;color:#333;margin-top:6px}
.contact-band{position:absolute;left:0;top:440px;width:400px;height:126px;background:var(--teal)}
.slant{position:absolute;left:0;top:428px}
.band-brand{position:absolute;top:22px;width:100%;text-align:center;font-size:13px;font-weight:600;letter-spacing:1px;color:#fff}
.band-sub{position:absolute;top:48px;width:100%;text-align:center;font-size:6px;font-style:italic;color:#d2ebe5}
.band-rule{position:absolute;top:72px;left:28px;right:28px;border-top:.5px solid #3a9886}
.get{position:absolute;left:28px;top:80px;font-size:5.2px;letter-spacing:.8px;color:#fff}
.get p{font-size:5.2px;letter-spacing:0;margin-top:5px;line-height:9px;color:#e1f0ec}
.follow{position:absolute;right:28px;top:82px;text-align:right;font-size:4.8px;font-weight:600;color:#fff;letter-spacing:.3px}
.follow div{display:flex;gap:4px;margin-top:4px}
.follow i{width:14px;height:14px;border:.8px solid #fff;border-radius:50%;display:block}
/* about */
.photo{position:absolute;left:28px;top:130px;width:344px;height:96px;border-radius:3px;background:linear-gradient(180deg,#b9bab6 0%,#8f918c 45%,#5d605c 100%)}
.node{position:absolute;display:flex;align-items:center;justify-content:center;border-radius:3px}
.node-owner{left:28px;top:334px;width:86px;height:36px;background:#fff;border:.6px solid #c9c9c5;font-size:8px;font-weight:500}
.node-pdp{left:149px;top:331px;width:101px;height:40px;background:var(--teal);color:#fff;font-size:8px;font-weight:600}
.node-sm{top:338px;width:27px;height:28px;background:#fff;border:.6px solid var(--teal);font-size:3.8px}
.col-label{position:absolute;top:319px;font-family:"IBM Plex Mono",monospace;font-size:5px;letter-spacing:1px;color:var(--teal)}
.pill{position:absolute;top:384px;height:16px;border:.6px solid #d0d0cc;border-radius:8px;background:#fff;display:flex;align-items:center;gap:4px;padding-left:4px;font-size:5px}
.num{width:8px;height:8px;border-radius:50%;background:var(--teal);color:#fff;font-size:4px;display:flex;align-items:center;justify-content:center;flex:none}
.objective{position:absolute;left:28px;top:417px;width:344px;height:49px;background:var(--teal-soft);border:.6px solid #c6dbd5;border-left:2.5px solid var(--teal);border-radius:3px;padding:6px 12px}
.objective p{font-size:5.8px;line-height:9px;color:#222;margin-top:4px}
/* services */
.services{position:absolute;left:28px;top:80px;display:grid;grid-template-columns:118px 118px 108px;row-gap:14px}
.svc{display:flex;gap:5px}
.svc .num{width:10px;height:10px;font-size:5px;margin-top:1px}
.svc b{display:block;font-size:5.8px;font-weight:400;color:#222}
.svc span{display:block;font-size:4.2px;line-height:5.6px;color:#777;margin-top:1px}
.roles{position:absolute;left:28px;top:272px;width:344px;border-collapse:collapse;font-size:5.5px}
.roles th{background:var(--teal);color:#fff;text-align:left;font-family:"IBM Plex Mono",monospace;font-weight:500;letter-spacing:1px;font-size:5px;height:18px;padding-left:9px}
.roles td{height:19px;padding-left:9px;border-bottom:.5px solid #e2e2de}
.roles td:first-child{color:var(--teal);border-right:.5px solid #d9d9d5}
.roles tr:nth-child(even) td{background:#f0f2ef}
.roles td:last-child{color:#444}
.list{position:absolute;top:418px;width:150px;list-style:none}
.list h4{font-size:9.5px;font-weight:600;margin-bottom:6px}
.list li{display:flex;gap:7px;font-size:5.2px;line-height:7.4px;color:#333;margin-bottom:5px}
.list svg{flex:none;margin-top:1px}
</style>
</head>
<body>

<section class="page p1">
  <div class="cover-photo" role="img" aria-label="Greyscale photo of a small onshore gas processing plant framed by solar panel arrays"></div>
  <div class="cover-brand"><span class="brand">CORVANTA</span></div>
  <div class="cover-kicker">PROJECT DELIVERY PARTNER &nbsp;·&nbsp; ENERGY &amp; RESOURCES</div>
  <h1 class="cover-title">Capability Statement</h1>
  <p class="cover-sub">Sharper Project Delivery, Steadier Operations.</p>
  <div class="stats">
    <div class="stat"><b>12</b><span>SERVICES</span></div>
    <div class="stat"><b>4</b><span>DIRECTORS</span></div>
    <div class="stat"><b>140+</b><span>YEARS EXP.</span></div>
  </div>
  <div class="cover-rule"></div>
  <div class="cover-url">www.corvanta.com.au</div>
</section>

<section class="page p2">
  <div class="runner"><span>CORVANTA</span><span>LEADERSHIP TEAM</span></div>
  <div class="abs eyebrow" style="left:28px;top:41px">OUR PEOPLE</div>
  <h2 class="abs" style="left:28px;top:50px">Key Personnel</h2>
  <p class="abs lead" style="left:28px;top:73px;font-size:5.6px">Senior leadership with decades of frontline and boardroom experience across the global energy industry.</p>

  <article class="card" style="left:28px;top:100px">
    <div class="card-head"><h3>Martin Hale</h3><p>Executive Director</p></div>
    <div class="card-body">
      <p class="card-exp">35 yrs experience — Northway, Kestrel Energy, Kelvane,<br><i>Ridgeline Energy</i></p>
      <p class="card-text">Extensive global energy industry experience, from frontline O&amp;M to the boardroom. Respected ‘C Suite’ leader with a track record of building high performing teams that deliver outstanding results.</p>
    </div>
  </article>
  <article class="card" style="left:207px;top:100px">
    <div class="card-head"><h3>Douglas Reid</h3><p>Technical Director</p></div>
    <div class="card-body">
      <p class="card-exp">39 yrs experience — Northway, Kestrel Energy,<br><i>Tarnhill Resources, Atlas Gas, Harbour Group, Solano Gas,</i></p>
      <p class="card-text">Highly skilled operations and project management professional delivering multiple projects and establishing best-in-class operational assets. Deep knowledge of project management, construction, commissioning and start-up, including a global functional assurance role.</p>
    </div>
  </article>
  <article class="card" style="left:28px;top:247px">
    <div class="card-head"><h3>Graham Pike</h3><p>Commercial Director</p></div>
    <div class="card-body">
      <p class="card-exp">40 yrs experience — Westhaven, Marlow Energy, Atlas Gas,<br><i>Kelvane, Ridgeline Energy</i></p>
      <p class="card-text">Senior Logistics, Supply Chain and Procurement Manager with strong operational, commercial, negotiating and relationship-building skills. Experienced in operating complex, diverse logistics operations — improving service levels while reducing cost.</p>
    </div>
  </article>
  <article class="card" style="left:207px;top:247px">
    <div class="card-head"><h3>Neil Ashdown</h3><p>Operations Director</p></div>
    <div class="card-body">
      <p class="card-exp">27 yrs experience — Atlas Gas, Harbour Group, Kelvane,<br><i>Solano Gas, Ridgeline Energy</i></p>
      <p class="card-text">27 years’ success leading operations, maintenance and commissioning teams on onshore and offshore oil and gas platforms, FPSOs, gas processing, coal seam gas, refrigeration and chemical refineries. Results-driven leader with a proven track record of delivery.</p>
    </div>
  </article>

  <svg class="slant" width="400" height="14" viewBox="0 0 400 14"><polygon points="0,14 400,0 400,14" fill="#d6d5d0"/><polygon points="0,14 400,6 400,14" fill="#087a68"/></svg>
  <div class="contact-band">
    <div class="band-brand">CORVANTA</div>
    <div class="band-sub">Sharper Project Delivery, Steadier Operations.</div>
    <div class="band-rule"></div>
    <div class="get">GET IN TOUCH<p>directors@corvanta.com.au<br>www.corvanta.com.au</p></div>
    <div class="follow">FOLLOW US<div><i></i><i></i><i></i></div></div>
  </div>
</section>

<section class="page p3">
  <div class="runner"><span>CORVANTA</span><span class="mono">ABOUT US &nbsp;·&nbsp; THE PARTNERSHIP MODEL</span></div>
  <div class="abs eyebrow" style="left:28px;top:38px">ABOUT US</div>
  <h2 class="abs" style="left:28px;top:47px">Who We Are</h2>
  <p class="abs lead" style="left:28px;top:72px;width:344px">Corvanta is a team of highly experienced Executive, Project, Construction, Commissioning and Operations specialists who combine deep technical knowledge with proven leadership to deliver unique Project Delivery Partner services to organisations across Australia. Our vision is straightforward: deliver projects clearly, run assets reliably.</p>
  <div class="photo" role="img" aria-label="Greyscale photo of gas processing pipework and plant equipment"></div>

  <div class="abs eyebrow" style="left:28px;top:237px">THE PARTNERSHIP MODEL</div>
  <h2 class="abs" style="left:28px;top:246px">What Is a Project Delivery Partner?</h2>
  <p class="abs lead" style="left:28px;top:270px;width:344px">A Project Delivery Partner (PDP) provides integrated project management, technical, commercial and delivery support that helps an organisation deliver a project successfully — acting as the owner’s team while the owner retains accountability and key decision-making authority.</p>

  <div class="col-label" style="left:61px">OWNER</div>
  <div class="col-label" style="left:153px">PROJECT DELIVERY PARTNER</div>
  <div class="col-label" style="left:293px">CONTRACTOR TEAMS</div>
  <div class="node node-owner">Operator XYZ</div>
  <div class="node node-pdp">CORVANTA</div>
  <div class="node node-sm" style="left:278px">Engineering</div>
  <div class="node node-sm" style="left:311px">Suppliers</div>
  <div class="node node-sm" style="left:344px">Execution</div>
  <svg class="abs" style="left:118px;top:346px" width="28" height="8"><line x1="0" y1="4" x2="24" y2="4" stroke="#9a9a96" stroke-width=".7"/><path d="M21 1.5 L25 4 L21 6.5" fill="none" stroke="#9a9a96" stroke-width=".7"/></svg>
  <svg class="abs" style="left:254px;top:346px" width="20" height="8"><line x1="0" y1="4" x2="16" y2="4" stroke="#9a9a96" stroke-width=".7"/><path d="M13 1.5 L17 4 L13 6.5" fill="none" stroke="#9a9a96" stroke-width=".7"/></svg>

  <div class="pill" style="left:24px;width:102px"><span class="num">1</span>Owner Controls the Project</div>
  <div class="pill" style="left:134px;width:123px"><span class="num">2</span>PDP Enables Delivery &amp; Assurance</div>
  <div class="pill" style="left:266px;width:110px"><span class="num">3</span>Contractors Execute the Work</div>

  <div class="objective">
    <div class="eyebrow" style="font-size:5px">PDP OBJECTIVE</div>
    <p>Deliver the project safely, on schedule, within budget and ready for operations — providing owner capability throughout the project lifecycle.</p>
  </div>
  <div class="folio"><span>CAPABILITY STATEMENT</span><span>02 / 04</span></div>
</section>

<section class="page p4">
  <div class="runner"><span>CORVANTA</span><span class="mono">OUR SERVICES &nbsp;·&nbsp; STRUCTURE &amp; VALUE</span></div>
  <div class="abs eyebrow" style="left:28px;top:38px">WHAT WE DELIVER</div>
  <h2 class="abs" style="left:28px;top:47px">Our Services</h2>
  <div class="services">
    <div class="svc"><span class="num">1</span><div><b>Project Management</b><span>Planning, reporting &amp; delivery leadership</span></div></div>
    <div class="svc"><span class="num">2</span><div><b>Engineering</b><span>Concept selection, design &amp; technical assurance</span></div></div>
    <div class="svc"><span class="num">3</span><div><b>Procurement</b><span>Contracting strategy, tender process &amp; management</span></div></div>
    <div class="svc"><span class="num">4</span><div><b>Approvals</b><span>Land access, permits, licences &amp; regulators</span></div></div>
    <div class="svc"><span class="num">5</span><div><b>Cost Control</b><span>Budget development, forecasting &amp; management</span></div></div>
    <div class="svc"><span class="num">6</span><div><b>Scheduling</b><span>Master schedule, WBS &amp; resource monitoring</span></div></div>
    <div class="svc"><span class="num">7</span><div><b>Risk Management</b><span>Register, identification, mitigation &amp; reporting</span></div></div>
    <div class="svc"><span class="num">8</span><div><b>Governance</b><span>Stage gates, change control &amp; decision support</span></div></div>
    <div class="svc"><span class="num">9</span><div><b>Construction</b><span>Management &amp; coordination of execution teams</span></div></div>
    <div class="svc"><span class="num">10</span><div><b>Commissioning &amp; Start-up</b><span>Completions system to steady-state</span></div></div>
    <div class="svc"><span class="num">11</span><div><b>Operations Readiness</b><span>People, process, systems &amp; technology</span></div></div>
    <div class="svc"><span class="num">12</span><div><b>Operations &amp; Maintenance</b><span>Minimise downtime &amp; lowest possible OPEX</span></div></div>
  </div>

  <div class="abs eyebrow" style="left:28px;top:230px">STRUCTURE</div>
  <h2 class="abs" style="left:28px;top:239px">Roles &amp; Responsibilities</h2>
  <table class="roles">
    <tr><th>OWNER</th><th>CORVANTA SERVICE</th></tr>
    <tr><td>Sets Project Objectives</td><td>Develops Delivery Plans</td></tr>
    <tr><td>Approves Major Decisions</td><td>Provides Recommendations</td></tr>
    <tr><td>Holds Project Risk</td><td>Identifies and Manages Risks</td></tr>
    <tr><td>Awards Contracts</td><td>Manages Contractor Interfaces</td></tr>
    <tr><td>Provides Funding</td><td>Monitors Cost and Schedule Performance</td></tr>
  </table>

  <div class="abs eyebrow" style="left:28px;top:396px;font-size:5px">WHY A PROJECT DELIVERY PARTNER</div>
  <ul class="list" style="left:28px;top:410px">
    <h4>PDP Benefits</h4>
    <li><svg width="9" height="9"><circle cx="4.5" cy="4.5" r="4.5" fill="#087a68"/><path d="M2.4 4.6 L4 6.1 L6.7 3" fill="none" stroke="#fff" stroke-width=".9"/></svg>Provides owners with access to experienced project delivery capability</li>
    <li><svg width="9" height="9"><circle cx="4.5" cy="4.5" r="4.5" fill="#087a68"/><path d="M2.4 4.6 L4 6.1 L6.7 3" fill="none" stroke="#fff" stroke-width=".9"/></svg>Improved project controls and governance</li>
    <li><svg width="9" height="9"><circle cx="4.5" cy="4.5" r="4.5" fill="#087a68"/><path d="M2.4 4.6 L4 6.1 L6.7 3" fill="none" stroke="#fff" stroke-width=".9"/></svg>Greater flexibility than traditional EPC delivery</li>
    <li><svg width="9" height="9"><circle cx="4.5" cy="4.5" r="4.5" fill="#087a68"/><path d="M2.4 4.6 L4 6.1 L6.7 3" fill="none" stroke="#fff" stroke-width=".9"/></svg>Enhanced visibility and management of cost, schedule and risk</li>
    <li><svg width="9" height="9"><circle cx="4.5" cy="4.5" r="4.5" fill="#087a68"/><path d="M2.4 4.6 L4 6.1 L6.7 3" fill="none" stroke="#fff" stroke-width=".9"/></svg>Scalable resources aligned with project phases</li>
  </ul>
  <ul class="list" style="left:210px;top:410px;width:162px">
    <h4>PDP Challenges</h4>
    <li><svg width="9" height="9"><circle cx="4.5" cy="4.5" r="4" fill="none" stroke="#b68b2e" stroke-width=".7"/><line x1="4.5" y1="4" x2="4.5" y2="6.6" stroke="#b68b2e" stroke-width=".8"/><circle cx="4.5" cy="2.7" r=".5" fill="#b68b2e"/></svg>Owner retains significant delivery risk</li>
    <li><svg width="9" height="9"><circle cx="4.5" cy="4.5" r="4" fill="none" stroke="#b68b2e" stroke-width=".7"/><line x1="4.5" y1="4" x2="4.5" y2="6.6" stroke="#b68b2e" stroke-width=".8"/><circle cx="4.5" cy="2.7" r=".5" fill="#b68b2e"/></svg>Requires clear governance and decision-making processes</li>
    <li><svg width="9" height="9"><circle cx="4.5" cy="4.5" r="4" fill="none" stroke="#b68b2e" stroke-width=".7"/><line x1="4.5" y1="4" x2="4.5" y2="6.6" stroke="#b68b2e" stroke-width=".8"/><circle cx="4.5" cy="2.7" r=".5" fill="#b68b2e"/></svg>Multiple contractor interfaces require strong coordination</li>
    <li><svg width="9" height="9"><circle cx="4.5" cy="4.5" r="4" fill="none" stroke="#b68b2e" stroke-width=".7"/><line x1="4.5" y1="4" x2="4.5" y2="6.6" stroke="#b68b2e" stroke-width=".8"/><circle cx="4.5" cy="2.7" r=".5" fill="#b68b2e"/></svg>Success depends on a collaborative Owner-PDP relationship</li>
  </ul>
  <div class="folio"><span>CAPABILITY STATEMENT</span><span>03 / 04</span></div>
</section>

</body>
</html>
```